Halvorsen Plumbing LLC business card

Would like a modern looking business card with my new logo

Contact Information for Business Card

Dwight Halvorsen 2417 Birchmont Hollow Rd Wrenford, QS 06512, Halvorsenplumbingllc@mailnest.example, 555-555-0184

```html
<!DOCTYPE html>
<html lang="en">
<head>
<meta charset="utf-8">
<title>Halvorsen Plumbing LLC – Business Card</title>
<link rel="stylesheet" href="https://fonts.googleapis.com/css2?family=Saira:wght@700&family=Lato:wght@400&display=swap">
<style>
  :root {
    --backdrop: #1c1c1e;
    --card-white: #ffffff;
    --brand-blue: #00aeef;
    --ink: #111111;
    --body-text: #464646;
  }
  * { box-sizing: border-box; margin: 0; padding: 0; }
  html, body {
    width: 1200px; height: 1200px; overflow: hidden;
    background: var(--backdrop);
  }
  .canvas { position: relative; width: 1200px; height: 1200px; }

  .card {
    position: absolute; left: 281px; width: 638px; height: 366px;
    border-radius: 27px; overflow: hidden;
  }
  .card--front { top: 195px; background: var(--card-white); }
  .card--back { top: 639px; background: var(--brand-blue); }

  .name-band {
    position: absolute; left: 0; top: 46px; width: 346px; height: 52px;
    background: var(--brand-blue);
    display: flex; align-items: center; padding-left: 38px;
  }
  .name-band__text {
    font-family: "Saira", sans-serif; font-weight: 700;
    font-size: 24px; letter-spacing: 0.5px; color: #fff; white-space: nowrap;
  }

  .wordmark {
    font-family: "Saira", sans-serif; font-weight: 700;
    color: var(--ink); text-align: center; line-height: 1;
  }
  .wordmark--front {
    position: absolute; left: 358px; top: 44px; width: 240px;
  }
  .wordmark--front .wordmark__main { font-size: 36px; }
  .wordmark--front .wordmark__sub { font-size: 14px; letter-spacing: 3px; margin-top: 3px; }

  .wordmark--back {
    position: absolute; left: 0; right: 0; top: 133px;
  }
  .wordmark--back .wordmark__main { font-size: 66px; }
  .wordmark--back .wordmark__sub { font-size: 24px; letter-spacing: 6px; margin-top: 6px; }

  .contact-list {
    position: absolute; left: 38px; top: 260px; list-style: none;
    font-family: "Lato", sans-serif; font-size: 16px; color: var(--body-text);
  }
  .contact-list__item { display: flex; align-items: center; height: 22px; white-space: nowrap; }
  .contact-list__icon { width: 14px; height: 14px; margin-right: 10px; fill: var(--brand-blue); flex: none; }

  .address {
    position: absolute; right: 40px; top: 260px; text-align: right;
    font-family: "Lato", sans-serif; font-size: 16px; line-height: 22px;
    color: var(--body-text); font-style: normal; white-space: nowrap;
  }
</style>
</head>
<body>
<main class="canvas">
  <section class="card card--front" aria-label="Business card front">
    <div class="name-band"><span class="name-band__text">DWIGHT HALVORSEN</span></div>
    <div class="wordmark wordmark--front">
      <div class="wordmark__main">HALVORSEN</div>
      <div class="wordmark__sub">PLUMBING LLC</div>
    </div>

    <ul class="contact-list">
      <li class="contact-list__item">
        <svg class="contact-list__icon" viewBox="0 0 24 24" aria-hidden="true"><path d="M6.6 10.8a15.1 15.1 0 0 0 6.6 6.6l2.2-2.2a1 1 0 0 1 1-.25 11.4 11.4 0 0 0 3.6.57 1 1 0 0 1 1 1V20a1 1 0 0 1-1 1A17 17 0 0 1 3 4a1 1 0 0 1 1-1h3.5a1 1 0 0 1 1 1c0 1.25.2 2.45.57 3.57a1 1 0 0 1-.25 1z"/></svg>
        555-555-0184
      </li>
      <li class="contact-list__item">
        <svg class="contact-list__icon" viewBox="0 0 24 24" aria-hidden="true"><path d="M2 5h20v14H2z"/><path d="M3.5 6.5 12 13l8.5-6.5" fill="none" stroke="#fff" stroke-width="1.6"/></svg>
        Halvorsenplumbingllc@mailnest.example
      </li>
      <li class="contact-list__item">
        <svg class="contact-list__icon" viewBox="0 0 24 24" aria-hidden="true"><circle cx="12" cy="12" r="10"/><path d="M2 12h20M12 2c3 3 3 17 0 20M12 2c-3 3-3 17 0 20" fill="none" stroke="#fff" stroke-width="1.5"/></svg>
        Halvorsenplumbingllc.example
      </li>
    </ul>

    <address class="address">
      Halvorsen Plumbing LLC<br>
      2417 Birchmont Hollow Rd<br>
      Wrenford, QS 06512
    </address>
  </section>

  <section class="card card--back" aria-label="Business card back">
    <div class="wordmark wordmark--back">
      <div class="wordmark__main">HALVORSEN</div>
      <div class="wordmark__sub">PLUMBING LLC</div>
    </div>
  </section>
</main>
</body>
</html>
```